Calvoreta Wine Label - Red Wine

We are a wine producing company based on the Oporto Metropolitan area.

We are looking to develop a label for a new red wine called "Calvoreta". Calvoreta is Portuguese for the well-known Spanish word Señorita, meaning a young lady. We want to make a label that reflects this young feeling with bright colours and fun designs while maintaining some elegance.

The target audience will be young people looking for a good time. Its preferred moments of consumption will be in social gatherings or fun times. We want to communicate fun.

We've attached the bottle model to be used, as well as some inspirational elements and our logo.
Updates

Low design quality

Target Market(s)

Young Consumers

Industry/Entity Type

Wine

Requirements
Must have
• Vintage year 2021, Red Wine mention

```html
<!DOCTYPE html>
<html lang="pt">
<head>
<meta charset="utf-8">
<title>Calvoreta — Douro DOC label</title>
<link href="https://fonts.googleapis.com/css2?family=Nunito+Sans:wght@400;800&display=swap" rel="stylesheet">
<style>
  :root {
    --paper: #ffffff;
    --label-edge: #f2f2f2;
    --ink: #0d0d0d;
    --coral: #e55e43;
    --salmon: #ef9282;
    --navy: #2f4e94;
    --mint: #90c9a5;
    --mustard: #e2ab12;
  }
  * { margin: 0; padding: 0; box-sizing: border-box; }
  html, body {
    width: 1200px;
    height: 1200px;
    overflow: hidden;
    background: var(--paper);
  }
  .canvas {
    position: relative;
    width: 1200px;
    height: 1200px;
    background: var(--paper);
    font-family: "Nunito Sans", sans-serif;
    color: var(--ink);
  }
  .label {
    position: absolute;
    left: 164px;
    top: 156px;
    width: 863px;
    height: 927px;
    background: var(--paper);
    outline: 1px solid var(--label-edge);
    overflow: hidden;
  }
  .artwork {
    position: absolute;
    left: 67px;
    top: 84px;
    width: 372px;
    height: 843px;
  }
  .producer {
    position: absolute;
    left: 539px;
    top: 72px;
    width: 192px;
    text-align: center;
    font-weight: 800;
    font-size: 26px;
    line-height: 1;
    white-space: nowrap;
  }
  .wine-name {
    position: absolute;
    left: 455px;
    top: 466px;
    width: 372px;
    text-align: center;
    font-weight: 800;
    font-size: 58px;
    line-height: 1;
    white-space: nowrap;
  }
  .appellation {
    position: absolute;
    left: 500px;
    top: 546px;
    width: 272px;
    text-align: center;
    font-weight: 400;
    font-size: 29px;
    line-height: 1;
  }
  .vintage {
    position: absolute;
    left: 500px;
    top: 640px;
    width: 272px;
    text-align: center;
    font-weight: 400;
    font-size: 22px;
    line-height: 1.4;
  }
  .region {
    position: absolute;
    left: 500px;
    top: 864px;
    width: 272px;
    text-align: center;
    font-weight: 400;
    font-size: 26px;
    line-height: 1;
  }
</style>
</head>
<body>
<main class="canvas">
  <section class="label">
    <svg class="artwork" viewBox="0 0 372 843" role="img"
         aria-label="Illustration area: a woman's profile silhouette filled with colourful portraits of diverse women">
      <defs>
        <linearGradient id="artwork-tones" x1="0" y1="0" x2="1" y2="1">
          <stop offset="0" stop-color="#2f4e94"/>
          <stop offset="0.3" stop-color="#e55e43"/>
          <stop offset="0.55" stop-color="#ef9282"/>
          <stop offset="0.75" stop-color="#90c9a5"/>
          <stop offset="1" stop-color="#e2ab12"/>
        </linearGradient>
      </defs>
      <path d="M0 843 L0 160 Q0 0 186 0 Q372 0 372 160 L372 843 Z" fill="url(#artwork-tones)"/>
    </svg>

    <div class="producer">Quinta Ravelo</div>
    <h1 class="wine-name">CALVORETA</h1>
    <p class="appellation">DOURO DOC</p>
    <p class="vintage">Red Wine<br>2021</p>
    <p class="region">Vinho Verde</p>
  </section>
</main>
</body>
</html>
```